Bref créative
business card for vegan prepared foods company
ZELO, taste the bright side
Simple
Petra Valdoni
Chef/Owner
www.zelofoods.example
zelofoods@mailbox.example
I would my business card to have on one side logo+web address, on the other side logo+ the rest of the info
logo and website address

```html
<!DOCTYPE html>
<html lang="en">
<head>
<meta charset="utf-8">
<title>Zelo business card</title>
<link rel="stylesheet" href="https://fonts.googleapis.com/css2?family=Open+Sans:wght@400;600;700&display=swap">
<style>
  :root {
    --bg: #e4e4e4;
    --brown: #7a6653;
    --green: #2fa84f;
    --white: #ffffff;
    --ink: #6b5a4a;
    --muted: #8a8a8a;
  }
  * { box-sizing: border-box; margin: 0; padding: 0; }
  html, body { width: 1200px; height: 895px; overflow: hidden; }
  body {
    background: var(--bg);
    font-family: "Open Sans", Arial, sans-serif;
    display: flex;
    align-items: center;
    justify-content: center;
    gap: 50px;
  }
  .card {
    width: 540px;
    height: 309px;
    position: relative;
    box-shadow: 0 8px 22px rgba(0,0,0,.18);
  }
  /* Front: info side */
  .card--info { background: var(--brown); padding: 16px; }
  .card--info .face {
    background: var(--white);
    width: 100%; height: 100%;
    display: flex;
    align-items: center;
    padding: 0 28px 0 34px;
  }
  .brand {
    width: 220px;
    display: flex;
    flex-direction: column;
    align-items: flex-start;
  }
  .brand-name {
    display: flex; align-items: center; gap: 10px;
    font-weight: 700; font-size: 46px; letter-spacing: 2px;
    color: var(--green); line-height: 1;
  }
  .brand-dot { width: 16px; height: 16px; border-radius: 50%; background: var(--green); }
  .brand-tagline { font-size: 13px; color: var(--muted); margin-top: 8px; }
  .divider { width: 1px; height: 140px; background: var(--ink); margin: 0 22px 0 30px; opacity: .6; }
  .contact { color: var(--ink); }
  .contact-name { font-size: 19px; font-weight: 600; }
  .contact-role { font-size: 12px; margin-bottom: 16px; }
  .contact-list { list-style: none; font-size: 12px; }
  .contact-list li { display: flex; align-items: center; gap: 8px; margin-bottom: 5px; }
  .contact-list svg { width: 14px; height: 14px; flex: none; }

  /* Back: logo side */
  .card--logo { background: var(--green); padding: 10px; }
  .card--logo .face {
    background: var(--brown);
    width: 100%; height: 100%;
    display: flex; flex-direction: column;
    align-items: center; justify-content: center;
  }
  .card--logo .brand-name { color: var(--white); font-size: 42px; }
  .card--logo .brand-dot { background: var(--green); }
  .card--logo .brand-tagline { color: #e9e2d9; font-size: 12px; }
  .web { color: var(--white); font-size: 14px; letter-spacing: 2px; margin-top: 40px; }
</style>
</head>
<body>
  <section class="card card--info">
    <div class="face">
      <div class="brand">
        <div class="brand-name"><span>ZELO</span><span class="brand-dot"></span></div>
        <div class="brand-tagline">taste the bright side</div>
      </div>
      <div class="divider"></div>
      <div class="contact">
        <div class="contact-name">Petra Valdoni</div>
        <div class="contact-role">Chef/Owner</div>
        <ul class="contact-list">
          <li><svg viewBox="0 0 14 14"><circle cx="7" cy="7" r="7" fill="#6b5a4a"/><path d="M4.5 3.8l1.4-.3.7 1.7-.9.6a5 5 0 0 0 2.5 2.5l.6-.9 1.7.7-.3 1.4C7 9.8 4.2 7 4.5 3.8z" fill="#fff"/></svg>555 014 2736</li>
          <li><svg viewBox="0 0 14 14"><circle cx="7" cy="7" r="7" fill="#6b5a4a"/><rect x="4.5" y="3" width="5" height="8" rx="1" fill="#fff"/></svg>555 018 4491</li>
          <li><svg viewBox="0 0 14 14"><circle cx="7" cy="7" r="7" fill="#6b5a4a"/><rect x="3.5" y="4.5" width="7" height="5" fill="#fff"/><path d="M3.5 4.5L7 7.3l3.5-2.8" fill="none" stroke="#6b5a4a" stroke-width=".8"/></svg>zelofoods@mailbox.example</li>
          <li><svg viewBox="0 0 14 14"><circle cx="7" cy="7" r="7" fill="#6b5a4a"/><circle cx="7" cy="7" r="3.5" fill="none" stroke="#fff" stroke-width=".9"/><path d="M3.5 7h7M7 3.5v7" stroke="#fff" stroke-width=".8"/></svg>www.zelofoods.example</li>
        </ul>
      </div>
    </div>
  </section>

  <section class="card card--logo">
    <div class="face">
      <div class="brand-name"><span>ZELO</span><span class="brand-dot"></span></div>
      <div class="brand-tagline">taste the bright side</div>
      <div class="web">www.zelofoods.example</div>
    </div>
  </section>
</body>
</html>
```